Publisher needs a book cover design for ‘Lanterns Over the Marsh Gate’ book

We need a book cover (front, back, spine) for the 2nd edition of a book entitled ‘Lanterns Over the Marsh Gate’ and subtitled ‘the quiet geography of tidal winds, ferry routes and harbour lanterns’ (inverted commas not to be part of the title and subtitle). The author is Rupert Calloway. The publisher is Vellmark Press. The finished size of the paperback version will be the industry standard 9" x 6". There will be paperback, hardback, and e-book versions. The final number of pages is expected to be in the region 150-180 pages. Text for the back cover is not yet available, but at the bottom of the back cover should be publisher logo (rectangular) on the left and space for the ISBN bar code on the right. The circular logo should be on the spine. The design should be original and not include any stock images that have been created by someone else or may require obtaining a copyright licence to use. Symbols in common use and not copyrighted are probably ok. There are no required images, photographs or symbols except the publisher logo at the left bottom of the back cover and lower spine. Spine lettering should be UK/US style with the top of the writing nearest the front cover. The designer is free to be creative using appropriate diagrams, symbols or abstract designs. Rectangular and circular variants of the publisher logo are attached. Designers are assured that when evaluating designs absolutely no notice whatsoever is taken of a designer's Pixo Rally ranking or status; We are completely output driven, so what matters is the design, not the ranking or status of the designer. In a similar way, designs are not evaluated as 'good' or 'bad' - the winning design will be chosen after review by a design review panel and is not decided arbitrarily by a single person. All submitted designs should be capable of effective copyright assignment.

Target Market(s)

Practitioners, parents, teachers, pupils and academics concerned with child protection, safeguarding and the elimination of emotional abuse of children in the classroom

Font styles to use
Serif
Sans Serif

Requirements
Must have
• • Title, author, edition, subtitle, publisher logo
Nice to have
• • Originality, innovation
Should not have
• • Stock images or anything else requiring additional copyright discussions and negotiations.

```html
<!DOCTYPE html>
<html lang="en">
<head>
<meta charset="utf-8">
<title>Lanterns Over the Marsh Gate — Cover</title>
<link href="https://fonts.googleapis.com/css2?family=League+Gothic&family=Abel&family=Cardo:wght@400&family=Questrial&display=swap" rel="stylesheet">
<style>
  :root {
    --back-grey: #d1d2d4;
    --panel-grey: #f2f2f2;
    --white: #ffffff;
    --ink: #1f1f1f;
    --red: #ed1c24;
    --plum: #7a2150;
    --navy: #2b2162;
    --badge-text: #4a1f5a;
  }
  html, body {
    margin: 0;
    padding: 0;
    width: 1200px;
    height: 872px;
    overflow: hidden;
    background: var(--back-grey);
  }
  .cover {
    position: relative;
    width: 1200px;
    height: 872px;
    background: var(--back-grey);
    overflow: hidden;
  }
  .back-blurb {
    position: absolute;
    left: 75px;
    top: 68px;
    width: 450px;
    margin: 0;
    font-family: "Abel", sans-serif;
    font-size: 27px;
    line-height: 36px;
    color: var(--ink);
  }
  .author-panel {
    position: absolute;
    left: 75px;
    top: 539px;
    width: 438px;
    height: 137px;
    background: var(--panel-grey);
  }
  .author-photo {
    position: absolute;
    left: 17px;
    top: 12px;
    width: 94px;
    height: 113px;
    background: var(--white);
  }
  .author-bio {
    position: absolute;
    left: 122px;
    top: 10px;
    width: 310px;
    margin: 0;
    font-family: "Cardo", serif;
    font-size: 12.6px;
    line-height: 15.7px;
    color: var(--ink);
  }
  .author-bio .label { display: block; font-size: 13.5px; }
  .publisher-mark {
    position: absolute;
    left: 77px;
    top: 716px;
    display: flex;
    align-items: center;
    gap: 8px;
  }
  .publisher-mark .dot {
    width: 44px;
    height: 44px;
    border-radius: 50%;
    background: var(--ink);
  }
  .publisher-mark .name {
    font-family: "Abel", sans-serif;
    font-size: 24px;
    letter-spacing: 1px;
    color: var(--ink);
  }
  .isbn-space {
    position: absolute;
    left: 384px;
    top: 697px;
    width: 129px;
    height: 84px;
    background: var(--white);
  }
  .artwork {
    position: absolute;
    left: 0;
    top: 0;
  }
</style>
</head>
<body>
<main class="cover">

  <p class="back-blurb">Lorem ipsum dolor sit amet, consectetur adipiscing elit, sed do eiusmod tempor incididunt ut labore et dolore magna aliqua. Ut enim ad minim veniam, quis nostrud exercitation ullamco laboris nisi ut aliquip ex ea commodo consequat. Duis aute irure dolor in reprehenderit in voluptate velit esse cillum dolore eu fugiat nulla pariatur. Excepteur sint occaecat cupidatat non proident, sunt in culpa qui officia deserunt mollit anim id est laborum.</p>

  <section class="author-panel">
    <div class="author-photo" role="img" aria-label="Author portrait placeholder"></div>
    <p class="author-bio"><span class="label">Author</span>Lorem ipsum dolor sit amet, consectetur adipiscing elit, sed do eiusmod tempor incididunt ut labore et dolore magna aliqua. Ut enim ad minim veniam, quis nostrud exercitation ullamco laboris nisi ut aliquip ex ea commodo consequat. Duis aute irure dolor in reprehenderit in voluptate</p>
  </section>

  <div class="publisher-mark">
    <span class="dot"></span>
    <span class="name">VELLMARK PRESS</span>
  </div>

  <div class="isbn-space"></div>

  <svg class="artwork" width="1200" height="872" viewBox="0 0 1200 872" xmlns="http://www.w3.org/2000/svg">
    <defs>
      <linearGradient id="front-fade" x1="0" y1="0" x2="0" y2="1">
        <stop offset="0" stop-color="#ed1c24"/>
        <stop offset="0.55" stop-color="#8a2049"/>
        <stop offset="1" stop-color="#2b2162"/>
      </linearGradient>
    </defs>

    <g class="spine" fill="#1f1f1f">
      <text class="spine-title" transform="translate(606,79) rotate(90)" font-family="League Gothic, sans-serif" font-size="28" letter-spacing="4" textLength="354" lengthAdjust="spacingAndGlyphs">LANTERNS OVER THE MARSH GATE</text>
      <text class="spine-subtitle" transform="translate(583,79) rotate(90)" font-family="Questrial, sans-serif" font-size="10.5" textLength="392" lengthAdjust="spacingAndGlyphs">The Quiet Geography of Tidal Winds, Ferry Routes and Harbour Lanterns</text>
      <text class="spine-edition" transform="translate(592,506) rotate(90)" font-family="Questrial, sans-serif" font-size="15" textLength="81" lengthAdjust="spacingAndGlyphs">2nd edition</text>
      <text class="spine-author" transform="translate(588,612) rotate(90)" font-family="League Gothic, sans-serif" font-size="30" textLength="148" lengthAdjust="spacingAndGlyphs">RUPERT CALLOWAY</text>
      <circle class="spine-mark" cx="600" cy="796" r="17"/>
    </g>

    <g class="front">
      <rect x="623" y="0" width="577" height="872" fill="url(#front-fade)"/>
      <rect class="top-band" x="683" y="0" width="443" height="58" fill="#fff"/>
      <rect class="bottom-band" x="683" y="842" width="443" height="30" fill="#fff"/>

      <g class="title" fill="#fff" font-family="League Gothic, sans-serif">
        <text x="686" y="196" font-size="150" textLength="438" lengthAdjust="spacingAndGlyphs">LANTERNS</text>
        <text x="686" y="345" font-size="160" textLength="438" lengthAdjust="spacingAndGlyphs">OVER THE</text>
        <text x="685" y="493" font-size="126" textLength="441" lengthAdjust="spacingAndGlyphs">MARSH GATE</text>
      </g>
      <rect class="title-rule" x="683" y="505" width="443" height="4" fill="#fff"/>

      <g class="subtitle" fill="#fff" font-family="League Gothic, sans-serif" font-size="34">
        <text x="703" y="563" textLength="406" lengthAdjust="spacingAndGlyphs">THE QUIET GEOGRAPHY OF TIDAL WINDS,</text>
        <text x="710" y="600" textLength="392" lengthAdjust="spacingAndGlyphs">FERRY ROUTES AND HARBOUR LANTERNS</text>
      </g>

      <g class="edition-badge">
        <circle cx="905" cy="690" r="55" fill="#fff"/>
        <text x="905" y="698" text-anchor="middle" font-family="League Gothic, sans-serif" font-size="62" fill="#4a1f5a">2nd</text>
        <text x="905" y="727" text-anchor="middle" font-family="League Gothic, sans-serif" font-size="30" fill="#4a1f5a">edition</text>
      </g>

      <text class="author-name" x="689" y="829" fill="#fff" font-family="League Gothic, sans-serif" font-size="88" textLength="434" lengthAdjust="spacingAndGlyphs">RUPERT CALLOWAY</text>
    </g>
  </svg>
</main>
</body>
</html>
```